The most modern business card ever !!!

Our company call “Vantilo”. Vantilo is a technology company specialized in cruises solutions. Out main product is a platform to reserve cruises. This is a revolutionary platform that make easier to travel agencies and final users to reserve cruises across dozen companies like tarvik, welbi, dpv, hbt, etc..We are a “start up”, with a young team of developers and we want to transmit it.. For it, we want something different, a modern business card that represent cruises and technology.. When someone receive this card, this person should say: wowww this is different… this is modern… this is a cruise related company..
Contact Information for Business Card
Requirements
Must have
- diferent, modern
Should not have
- traditions business card

```html
<!DOCTYPE html>
<html lang="en">
<head>
<meta charset="utf-8">
<title>Vantilo — Business Card</title>
<link rel="stylesheet" href="https://fonts.googleapis.com/css2?family=Montserrat:wght@300;400;600;800&display=swap">
<style>
  :root {
    --backdrop: #e4e4e4;
    --card-white: #fbfdff;
    --ice-blue: #bfe2f5;
    --sky-blue: #8ccbec;
    --brand-blue: #2c9be0;
    --band-black: #1f1f21;
    --ink: #1c1c1e;
    --band-text: #d9d9d9;
  }
  * { margin: 0; padding: 0; box-sizing: border-box; }
  html, body { width: 1200px; height: 801px; overflow: hidden; }
  body {
    background: var(--backdrop);
    font-family: "Montserrat", sans-serif;
    position: relative;
  }
  .card {
    position: absolute;
    top: 160px;
    width: 480px;
    height: 480px;
    border-radius: 40px;
    overflow: hidden;
    background: radial-gradient(circle at 50% 50%, var(--card-white) 0%, var(--card-white) 30%, var(--ice-blue) 68%, var(--sky-blue) 100%);
  }
  .card--front { left: 90px; }
  .card--back { left: 630px; }

  .wave-field {
    position: absolute;
    inset: 0;
  }

  .brand-name {
    position: absolute;
    left: 0; right: 0;
    top: 50%;
    transform: translateY(-50%);
    text-align: center;
    font-size: 64px;
    font-weight: 600;
    letter-spacing: 1px;
    color: var(--ink);
  }

  .band {
    position: absolute;
    left: 0; right: 0;
    height: 78px;
    background: var(--band-black);
    color: var(--band-text);
    display: flex;
    align-items: center;
    justify-content: center;
    font-size: 18px;
    letter-spacing: 3px;
    font-weight: 300;
  }
  .band--top { top: 0; text-transform: uppercase; }
  .band--bottom { bottom: 0; letter-spacing: 2px; }

  .contact {
    position: absolute;
    top: 78px; bottom: 78px; left: 0; right: 0;
    display: flex;
    flex-direction: column;
    align-items: center;
    justify-content: center;
    gap: 10px;
    color: var(--ink);
  }
  .contact__name {
    font-size: 40px;
    font-weight: 800;
    color: var(--brand-blue);
    letter-spacing: 2px;
    text-transform: uppercase;
  }
  .contact__role {
    font-size: 17px;
    font-weight: 400;
    margin-bottom: 14px;
  }
  .contact__line {
    display: flex;
    flex-direction: column;
    align-items: center;
    gap: 6px;
    font-size: 15px;
    font-weight: 400;
  }
  .contact__icon { width: 22px; height: 22px; }
  .contact__email { margin-top: 8px; font-size: 15px; }
</style>
</head>
<body>
  <section class="card card--front">
    <div class="wave-field" role="img" aria-label="Soft geometric pattern of layered pale blue squares radiating from the centre"></div>
    <div class="brand-name">Vantilo</div>
  </section>

  <section class="card card--back">
    <div class="band band--top">Contact</div>
    <div class="contact">
      <div class="contact__name">Elias Moreno</div>
      <div class="contact__role">Director of Operations</div>
      <div class="contact__line">
        <svg class="contact__icon" viewBox="0 0 24 24" aria-hidden="true">
          <circle cx="12" cy="12" r="12" fill="#1f1f21"/>
          <path d="M8.5 6.5c.4-.4 1-.4 1.3 0l1.2 1.6c.3.4.2.9-.1 1.2l-.8.7c.6 1.3 1.6 2.3 2.9 2.9l.7-.8c.3-.3.8-.4 1.2-.1l1.6 1.2c.4.3.4.9 0 1.3l-.9.9c-.6.6-1.6.7-2.4.3-2.5-1.3-4.4-3.2-5.7-5.7-.4-.8-.3-1.8.3-2.4z" fill="#fff"/>
        </svg>
        <span>415 702 3388</span>
      </div>
      <div class="contact__line contact__email">
        <svg class="contact__icon" viewBox="0 0 24 24" aria-hidden="true">
          <circle cx="12" cy="12" r="12" fill="#1f1f21"/>
          <rect x="6.5" y="8" width="11" height="8" rx="1" fill="none" stroke="#fff" stroke-width="1.4"/>
          <path d="M6.8 8.5 12 12.6l5.2-4.1" fill="none" stroke="#fff" stroke-width="1.4"/>
        </svg>
        <span>elias@vantilo.io</span>
      </div>
    </div>
    <div class="band band--bottom">www.vantilo.com</div>
  </section>
</body>
</html>
```